Business card for a plastic surgeon

i need a business card for a plastic surgeon. I have two adresses. The card should communicate safety, simmetry, beauty and with soft colors.
What i want in the card:
- my logo: Letters "R"and "B" (picture uploaded)
- my name: Renato Bastiani
- my registration: CRM 507 219
- my adresses and phone numbers (2):
- Av Dr Teixeira Lopes, 2710, sala 305 - Vila Olímpia | São Paulo/ SP - Phone: 11 4172-5036
- Al. Itapeva, 47, 3 andar - Alphaville | Barueri/ SP - Phone: 11 6350-2481

- my social network: site, facebook and instagram

Target Market(s)

people (95% girls and women) that want cosmetic procedures and plastic surgery

Industry/Entity Type

Business

Contact Information for Business Card

The card should communicate safety, simmetry, beauty and with soft colors.
Beige, brown, gray, rosy are some options. Color is free

Font styles to use
Serif

Requirements
Must have
• - my logo: Letters "R"and "B" (picture uploaded)
• - my name: Renato Bastiani
• - my registration: CRM 507 219
• - my adresses and phone numbers (2):
• - Av Dr Teixeira Lopes, 2710, sala 305 - Vila Olímpia | São Paulo/ SP - Phone: 11 4172-5036
• - Al. Itapeva, 47, 3 andar - Alphaville | Barueri/ SP - Phone: 11 6350-2481
• - my social network: site, facebook and instagram
Should not have
• other images (only my logo)

```html
<!DOCTYPE html>
<html lang="pt-BR">
<head>
<meta charset="utf-8">
<title>Renato Bastiani – Business Card</title>
<link rel="stylesheet" href="https://fonts.googleapis.com/css2?family=Roboto:wght@300;400;500;700&family=Cormorant+Garamond:wght@500&display=swap">
<style>
  :root {
    --page-bg: #e9e4df;
    --card-dark: #0c0c0c;
    --card-mid: #2a2a2a;
    --accent-beige: #c8ab91;
    --text-light: #e6e3df;
    --icon-grey: #8a8580;
  }
  * { box-sizing: border-box; margin: 0; padding: 0; }
  html, body {
    width: 1200px; height: 1000px; overflow: hidden;
    background: var(--page-bg);
    font-family: "Roboto", Arial, sans-serif;
  }
  .card {
    position: absolute;
    width: 620px; height: 354px;
    border-radius: 4px;
    background: linear-gradient(135deg, var(--card-dark) 0%, #151515 45%, var(--card-mid) 100%);
    box-shadow: 0 14px 30px rgba(0,0,0,0.25);
    color: var(--text-light);
  }
  .card-front { left: 60px; top: 90px; }
  .card-back { left: 520px; top: 556px; }

  .monogram {
    position: absolute;
    font-family: "Cormorant Garamond", Georgia, serif;
    font-weight: 500;
    color: var(--accent-beige);
    letter-spacing: 2px;
  }
  .card-front .monogram { left: 462px; top: 30px; font-size: 40px; }
  .card-back .monogram { left: 0; right: 0; top: 118px; text-align: center; font-size: 92px; line-height: 1; }

  .holder-name {
    position: absolute; left: 52px; top: 140px;
    font-size: 22px; font-weight: 700; letter-spacing: 1px;
    color: var(--accent-beige);
    text-transform: uppercase;
  }
  .registration {
    position: absolute; left: 52px; top: 172px;
    font-size: 12.5px; font-weight: 400; letter-spacing: 1px;
    color: var(--text-light);
  }
  .addresses { position: absolute; left: 52px; top: 212px; font-size: 12.5px; font-weight: 300; line-height: 1.4; }
  .address + .address { margin-top: 14px; }
  .address-label { color: var(--accent-beige); font-weight: 400; }

  .contacts { position: absolute; left: 390px; top: 140px; list-style: none; font-size: 13px; font-weight: 300; }
  .contacts li { display: flex; align-items: flex-start; gap: 8px; line-height: 1.35; margin-bottom: 4px; }
  .contact-icon { flex: none; width: 15px; height: 15px; margin-top: 1px; }
  .contact-dot { flex: none; width: 15px; height: 15px; border-radius: 50%; background: var(--icon-grey); margin-top: 1px; }
  .web-accent { color: var(--accent-beige); }
</style>
</head>
<body>
  <section class="card card-front" aria-label="Card front">
    <div class="monogram">RB</div>
    <h1 class="holder-name">Renato Bastiani</h1>
    <p class="registration">CRM 507 219</p>
    <div class="addresses">
      <p class="address"><span class="address-label">Address 1:</span><br>Av Dr Teixeira Lopes, 2710, sala 305<br>Vila Olimpia&nbsp; Sao Paulo/ SP</p>
      <p class="address"><span class="address-label">Address 2:</span><br>Al. Itapeva, 47, 3 andar<br>Alphaville&nbsp; Barueri/ SP</p>
    </div>
    <ul class="contacts">
      <li>
        <svg class="contact-icon" viewBox="0 0 16 16" aria-hidden="true">
          <circle cx="8" cy="8" r="7" fill="var(--icon-grey)"/>
          <g fill="none" stroke="#1a1a1a" stroke-width="0.9">
            <circle cx="8" cy="8" r="5.5"/><ellipse cx="8" cy="8" rx="2.4" ry="5.5"/>
            <line x1="2.5" y1="8" x2="13.5" y2="8"/>
          </g>
        </svg>
        <span>www.<span class="web-accent">clinicabastiani</span>.com.br</span>
      </li>
      <li><span class="contact-dot"></span><span>/renatobastiani</span></li>
      <li><span class="contact-dot"></span><span>/renatobastiani</span></li>
      <li>
        <svg class="contact-icon" viewBox="0 0 16 16" aria-hidden="true">
          <circle cx="8" cy="8" r="7" fill="var(--icon-grey)"/>
          <path d="M5.6 4.5l1.4-.3.8 2-1 .8a5 5 0 0 0 2.2 2.2l.8-1 2 .8-.3 1.4c-3.5.3-6.2-2.4-5.9-5.9z" fill="#1a1a1a"/>
        </svg>
        <span>+55 11 4172 5036<br>+55 11 6350 2481</span>
      </li>
    </ul>
  </section>

  <section class="card card-back" aria-label="Card back">
    <div class="monogram">RB</div>
  </section>
</body>
</html>
```